A Dedicated Thank You to my Dad

Proposed Dimensions: Approx. 20" x 30"

For Father's Day, I wrote a dedication to my Dad that encapsulates my gratitude for everything he does, and everything he is. His birthday is on August 3, but it is more important for me to transform this dedication into a meaningful and memorable gift than to meet any deadline. I would love an image that captures the relationship between a father and his son, accompanied by my words of thanks in some sort of font that is appropriate for the message (calligprahy? not sure about that).

I had actually posted the Thank You on Pixelmarrow as a public post, so anyone with an account can read it: https://www.pixelmarrow.example/photo.php?fbid=40872219360548813&set=a.318760942157.6650129.3908471&type=1&theater

Only the words starting with "Thank you ..." should be on the poster.

Target Market(s)

This is a personal gift for my Dad. He doesn't have the best of eyesight, so having the words in a really small font would not be particularly helpful. :-)

Requirements
Must have
• * Personable
* Warm
* Inviting
* Memorable
* Understated more favored over Loud
Should not have
• * An entire palette of colors
* Wacky colors or fonts

```html
<!DOCTYPE html>
<html lang="en">
<head>
<meta charset="utf-8">
<title>A Thank You to Dad</title>
<link rel="stylesheet" href="https://fonts.googleapis.com/css2?family=Great+Vibes&family=Petit+Formal+Script&display=swap">
<style>
  :root {
    --backdrop: #e9e8e6;
    --paper-light: #cdc1b3;
    --paper-dark: #b8aa9a;
    --ink: #1d1611;
    --photo-light: #cbbba8;
    --photo-dark: #3a2d24;
    --ornament: #2a211b;
  }
  * { margin: 0; padding: 0; box-sizing: border-box; }
  html, body {
    width: 1200px;
    height: 1148px;
    overflow: hidden;
    background: var(--backdrop);
  }
  .poster {
    position: absolute;
    left: 240px;
    top: 54px;
    width: 720px;
    height: 1040px;
    overflow: hidden;
    background: radial-gradient(ellipse at 40% 35%, var(--paper-light), var(--paper-dark));
    color: var(--ink);
    box-shadow: 0 0 0 1px rgba(0,0,0,0.08);
  }
  .ornament {
    position: absolute;
    width: 110px;
    height: 110px;
    background: var(--ornament);
    opacity: 0.85;
    clip-path: polygon(0 0, 100% 0, 100% 100%);
  }
  .ornament--top-right { top: 18px; right: 18px; }
  .ornament--bottom-left {
    bottom: 18px; left: 18px;
    clip-path: polygon(0 0, 0 100%, 100% 100%);
  }
  .greeting {
    position: absolute;
    left: 100px;
    top: 40px;
    font-family: "Great Vibes", cursive;
    font-size: 104px;
    line-height: 1;
  }
  .message {
    position: absolute;
    left: 0;
    width: 100%;
    font-family: "Petit Formal Script", cursive;
    font-size: 26px;
    line-height: 60px;
    white-space: nowrap;
  }
  .message--opening { top: 100px; text-align: center; padding-left: 20px; }
  .message--opening .lead { display: block; text-align: right; padding-right: 70px; }
  .message--closing { top: 505px; text-align: left; padding-left: 90px; }
  .message--closing .tail { padding-left: 10px; }
  .signature {
    position: absolute;
    left: 135px;
    top: 810px;
    font-family: "Great Vibes", cursive;
    font-size: 56px;
    line-height: 1;
  }
  .portrait {
    position: absolute;
    left: 295px;
    top: 715px;
    width: 425px;
    height: 325px;
    background: radial-gradient(ellipse at 55% 40%, var(--photo-light), var(--photo-dark));
    border-top-left-radius: 60% 40%;
  }
</style>
</head>
<body>
  <main class="poster">
    <div class="ornament ornament--top-right" role="img" aria-label="Floral corner ornament"></div>

    <h1 class="greeting">Daddy</h1>

    <p class="message message--opening">
      <span class="lead">Thank you for</span>
      always carrying us to the car after we fell<br>
      asleep, even after we were definitely old<br>
      enough to walk it. Thank you for<br>
      welcoming more people to stay with us<br>
      than I can count.
    </p>

    <p class="message message--closing">
      Thank you for never giving up on trying<br>
      to convince me that imperfection is not a<br>
      failure. Thank you for teaching me to try<br>
      to find the good in<br>
      <span class="tail">everyone.</span>
    </p>

    <p class="signature">Owen</p>

    <div class="portrait" role="img" aria-label="Sepia engraved-style photo of a son and his father standing arm in arm"></div>

    <div class="ornament ornament--bottom-left" role="img" aria-label="Floral corner ornament"></div>
  </main>
</body>
</html>
```